Beautiful Quotes For Social Media Posts

We are looking for 5 beautifully designed quotes for our social media account.

Inspiration of styles we like in both style and color along with a few of our favorite fonts (you are NOT limited to these fonts this is just to give you an idea):
https://morrowstudio.example.net/s/k7p2q9x4m1t8v3n6b5c0z2w8y4j1

*These fonts are property of Morrow Studio. You do not have permission/rights to use them outside of this assignment*

Quotes to use (5):
“Only those who dare to fail greatly can ever achieve greatly.” –Walter J. Simmons
“Don’t go through life, grow through life.” – Neil Ashcombe
“Follow your bliss and the universe will open doors where there were only walls.” – Martin Oakley
“If you don’t like the road you’re walking, start paving another one.” – Greta Vance
“Life is like riding a bicycle. To keep your balance, you must keep moving.” —Oskar Feldmann

File Specifics:
- JPG
- 10x10 in size (square)
- Please include @MorrowStudio in the bottom right left or center of each design

Brand Details:
Soft but rich pastel and bright colors.
Hand Drawn florals, doodles and art
Handwritten looking fonts
Artsy, Creative, Girl and Inspiring

```html
<!DOCTYPE html>
<html lang="en">
<head>
<meta charset="utf-8">
<title>Quote Post Series</title>
<link href="https://fonts.googleapis.com/css2?family=Plus+Jakarta+Sans:wght@700;800&family=Montserrat:wght@900&display=swap" rel="stylesheet">
<style>
  :root {
    --page: #dfdfdf;
    --ink: #1c1c1c;
    --white: #ffffff;
    --plum: #7a1f4a;
    --plum-dark: #2a0a3a;
    --crimson: #9a0c2c;
    --teal: #0e4a6a;
    --navy: #0a2284;
    --navy-dark: #061660;
    --night: #220a36;
    --berry: #4c0f3e;
    --magenta: #b0084e;
    --sky: #1a7ac0;
  }
  * { margin: 0; padding: 0; box-sizing: border-box; }
  html, body { width: 1200px; height: 3000px; overflow: hidden; }
  body {
    position: relative;
    background: var(--page);
    font-family: "Plus Jakarta Sans", Arial, sans-serif;
    font-weight: 700;
  }
  .post {
    position: absolute;
    left: 332px;
    width: 536px;
    height: 536px;
    overflow: hidden;
    box-shadow: 0 6px 18px rgba(0,0,0,0.22);
  }
  .post > * { position: absolute; }
  .mark {
    font-family: "Montserrat", Arial, sans-serif;
    font-weight: 900;
    font-size: 150px;
    line-height: 1;
    height: 80px;
  }
  .quote, .author, .handle { left: 0; width: 100%; text-align: center; white-space: nowrap; }
  .handle { font-size: 16px; line-height: 20px; }

  /* Post 1 */
  .post-dare { top: 55px; background: linear-gradient(160deg, var(--plum-dark) 0%, #3c0a34 50%, var(--crimson) 100%); }
  .post-dare .panel { left: 28px; top: 26px; width: 480px; height: 483px; background: linear-gradient(135deg, #f6f6f6, #e6e6e6); }
  .post-dare .mark { left: 0; width: 100%; text-align: center; top: 117px; color: var(--plum); }
  .post-dare .quote { top: 228px; font-size: 35px; line-height: 41px; color: var(--ink); }
  .post-dare .author { top: 374px; font-size: 26px; color: var(--plum); }
  .post-dare .handle { top: 470px; color: var(--plum); }

  /* Post 2 */
  .post-grow { top: 636px; background: linear-gradient(135deg, #f7f7f7, #e8e8e8); }
  .post-grow .frame { left: 28px; top: 27px; width: 479px; height: 481px; border: 3px solid #111; }
  .post-grow .mark { left: 0; width: 100%; text-align: center; top: 133px; color: var(--teal); }
  .post-grow .quote { top: 243px; font-size: 35px; line-height: 41px; color: var(--ink); }
  .post-grow .author { top: 361px; font-size: 26px; color: var(--teal); }
  .post-grow .handle { top: 468px; left: 50px; width: auto; text-align: left; color: var(--teal); }

  /* Post 3 */
  .post-bliss { top: 1226px; background: radial-gradient(circle at 50% 50%, var(--navy) 0%, #0a1e78 55%, var(--navy-dark) 100%); }
  .post-bliss .mark { left: 0; width: 100%; text-align: center; top: 119px; color: var(--white); }
  .post-bliss .quote { top: 236px; font-size: 27px; line-height: 32px; color: var(--white); }
  .post-bliss .author { top: 364px; font-size: 27px; color: var(--white); }
  .post-bliss .handle { top: 494px; color: var(--white); }

  /* Post 4 */
  .post-road { top: 1813px; background: linear-gradient(160deg, #2a0a36 0%, var(--night) 55%, #170826 100%); }
  .post-road .frame { left: 56px; top: 170px; width: 419px; height: 218px; border: 2px solid var(--white); }
  .post-road .mark { left: 86px; top: 76px; color: var(--white); }
  .post-road .quote { left: 89px; width: 380px; top: 238px; text-align: left; font-size: 26px; line-height: 32px; color: var(--white); }
  .post-road .author { left: 84px; width: auto; top: 371px; padding: 0 4px; font-size: 26px; color: var(--white); background: #200a33; }
  .post-road .handle { top: 494px; color: var(--white); }

  /* Post 5 */
  .post-balance { top: 2405px; background: var(--white); }
  .post-balance .frame { left: 28px; top: 27px; width: 479px; height: 474px; border: 3px solid var(--sky); }
  .post-balance .card { left: 79px; top: 164px; width: 407px; height: 226px; background: var(--magenta); border-radius: 38px 38px 0 50px; }
  .post-balance .badge { left: 46px; top: 120px; width: 104px; height: 104px; border-radius: 50%; background: var(--sky); border: 5px solid var(--white); }
  .post-balance .badge span { position: absolute; left: 0; width: 100%; text-align: center; top: 4px; font-family: "Montserrat", Arial, sans-serif; font-weight: 900; font-size: 100px; line-height: 1; color: var(--white); }
  .post-balance .quote { left: 139px; width: auto; top: 218px; text-align: left; font-size: 23px; line-height: 30px; color: var(--white); }
  .post-balance .author { left: 139px; width: auto; top: 328px; font-size: 23px; color: var(--white); }
  .post-balance .handle { top: 462px; color: var(--sky); }
</style>
</head>
<body>

<section class="post post-dare">
  <svg width="536" height="536" style="left:0;top:0" role="img" aria-label="Abstract red light streaks">
    <polygon points="0,460 200,536 0,536" fill="#c0102c" opacity="0.6"/>
    <circle cx="520" cy="360" r="50" fill="#e0204a" opacity="0.7"/>
  </svg>
  <div class="panel" role="img" aria-label="Soft white sculpted texture background"></div>
  <div class="mark">“</div>
  <p class="quote">Only those who dare to<br>fail greatly can ever<br>achieve greatly</p>
  <p class="author">- Walter J. Simmons</p>
  <p class="handle">@MorrowStudio</p>
</section>

<section class="post post-grow">
  <div class="frame"></div>
  <svg width="536" height="536" style="left:0;top:0" role="img" aria-label="Black brush stroke accents in opposite corners">
    <polygon points="0,0 280,0 0,175" fill="#111"/>
    <polygon points="536,345 536,536 350,536" fill="#111"/>
  </svg>
  <div class="mark">“</div>
  <p class="quote">Don’t go through life,<br>grow through life</p>
  <p class="author">- Neil Ashcombe</p>
  <p class="handle">@MorrowStudio</p>
</section>

<section class="post post-bliss">
  <svg width="536" height="536" style="left:0;top:0">
    <circle cx="268" cy="267" r="201" fill="none" stroke="#ffffff" stroke-width="2" stroke-dasharray="8 6"/>
  </svg>
  <div class="mark">“</div>
  <p class="quote">Follow your bliss and the<br>universe will open doors<br>where there were only walls</p>
  <p class="author">- Martin Oakley</p>
  <p class="handle">@MorrowStudio</p>
</section>

<section class="post post-road">
  <svg width="536" height="536" style="left:0;top:0">
    <circle cx="437" cy="38" r="84" fill="var(--berry)"/>
    <circle cx="560" cy="200" r="70" fill="none" stroke="#4a0f3e" stroke-width="26"/>
    <circle cx="520" cy="320" r="90" fill="#2e0c3c"/>
  </svg>
  <div class="frame"></div>
  <div class="mark">“</div>
  <p class="quote">If you don’t like the road<br>you’re walking, start paving<br>another one</p>
  <p class="author">- Greta Vance</p>
  <p class="handle">@MorrowStudio</p>
</section>

<section class="post post-balance">
  <div class="frame"></div>
  <svg width="536" height="536" style="left:0;top:0" role="img" aria-label="Colourful geometric triangle clusters in two corners">
    <defs>
      <linearGradient id="tri" x1="0" y1="0" x2="1" y2="1">
        <stop offset="0" stop-color="#e0104a"/>
        <stop offset="0.5" stop-color="#f0a020"/>
        <stop offset="1" stop-color="#c0083a"/>
      </linearGradient>
    </defs>
    <polygon points="380,0 536,0 536,190 470,120" fill="url(#tri)"/>
    <polygon points="0,370 0,536 145,500" fill="url(#tri)"/>
    <polygon points="440,200 470,240 420,230" fill="#3aa8e0"/>
    <polygon points="65,405 90,420 65,440" fill="#3aa8e0"/>
  </svg>
  <div class="card"></div>
  <div class="badge"><span>“</span></div>
  <p class="quote">Life is like riding a bicycle.<br>To keep your balance, you<br>must keep moving.</p>
  <p class="author">- Oskar Feldmann</p>
  <p class="handle">@MorrowStudio</p>
</section>

</body>
</html>
```